Business Card design for shipping company 'FERNHOLT INTERNATIONAL LTD'

Classic / traditional business card in black Garamond / Times New Roman or similar text for a shipping / marine transport company, containing the following information:

QUOTE

FERNHOLT INTERNATIONAL LTD

MARTIN QUESTEDGE FICS

T: +44 7902 615370
E: cargo@fernholt-example.com

UNQUOTE

Target Market(s)

Marine / Shipping industry

Contact Information for Business Card

FERNHOLT INTERNATIONAL LTD MARTIN QUESTEDGE FICS T: +44 7902 615370 E: cargo@fernholt-example.com

Font styles to use
Serif

Colors

Designer to choose colors to be used in the design.

Requirements
Must have
• Garamond / Times New Roman or similar text in black colour

```html
<!DOCTYPE html>
<html lang="en">
<head>
<meta charset="utf-8">
<title>Fernholt International Ltd – Business Card</title>
<link rel="stylesheet" href="https://fonts.googleapis.com/css2?family=Tinos:ital,wght@0,400;0,700;1,700&display=swap">
<style>
  :root {
    --backdrop: #717171;
    --card: #ffffff;
    --ink: #000000;
  }
  * { margin: 0; padding: 0; box-sizing: border-box; }
  html, body {
    width: 1200px;
    height: 1000px;
    overflow: hidden;
    background: var(--backdrop);
  }
  .stage {
    position: relative;
    width: 1200px;
    height: 1000px;
  }
  .business-card {
    position: absolute;
    left: 283px;
    top: 330px;
    width: 613px;
    height: 352px;
    background: var(--card);
    color: var(--ink);
    font-family: "Tinos", "Times New Roman", serif;
  }
  .brand {
    position: absolute;
    left: 47px;
    top: 45px;
    display: flex;
    align-items: center;
    gap: 12px;
  }
  .brand-mark {
    width: 51px;
    height: 51px;
    display: block;
  }
  .brand-name {
    font-weight: 700;
    font-size: 22px;
    letter-spacing: 2.1px;
    line-height: 1;
    white-space: nowrap;
    padding-top: 3px;
  }
  .holder-name {
    position: absolute;
    left: 0;
    right: 0;
    top: 160px;
    text-align: center;
    font-weight: 700;
    font-style: italic;
    font-size: 24px;
    line-height: 1;
    padding-left: 1px;
  }
  .contact {
    position: absolute;
    left: 0;
    right: 0;
    top: 280px;
    text-align: center;
    font-size: 17px;
    line-height: 22px;
    letter-spacing: 0.4px;
  }
  .contact p { margin: 0; }
</style>
</head>
<body>
  <main class="stage">
    <section class="business-card" aria-label="Fernholt International Ltd business card">
      <header class="brand">
        <svg class="brand-mark" viewBox="0 0 51 51" aria-hidden="true">
          <circle cx="25.5" cy="25.5" r="24" fill="none" stroke="var(--ink)" stroke-width="2"/>
        </svg>
        <span class="brand-name">FERNHOLT INTERNATIONAL LTD</span>
      </header>

      <h1 class="holder-name">Martin Questedge Fics</h1>

      <address class="contact" style="font-style: normal;">
        <p class="contact-phone">+44 7902 615370</p>
        <p class="contact-email">cargo@fernholt-example.com</p>
      </address>
    </section>
  </main>
</body>
</html>
```